A5, portrait
Theme is science
audience is VIPS, politicians, executives
this is a really important event, we want a very classy invitation
include logo for bloom and grow and lumen but lumen one bigger
images attached
Have attached some styles we like but doesn't need to be these colours. If we can incorporate some colours from our logo would be good but don't make too colourful and childish

You’re invited to the official opening and launch of Lumen, Centre of Discovery. an industry first, pioneering, STEM hub.

Saturday 30th April, 2022

10:00 am – 12:00 pm

42 Calder Lane, Wrenfield

Light canapes provided. Dress code is smart/casual

All guests will be given a guided walk through of Australia’s first dedicated STEM education hub for children aged 3-6.

Invitation only

RSVP: 18 April to marketing@bloomandgrow.edu.au

```html
<!DOCTYPE html>
<html lang="en">
<head>
<meta charset="utf-8">
<title>Lumen, Centre of Discovery: Official Opening Invitation</title>
<link rel="stylesheet" href="https://fonts.googleapis.com/css2?family=Lato:ital,wght@0,400;0,900;1,700&family=Lobster+Two:ital,wght@1,700&family=Jost:wght@400&family=Lobster&display=swap">
<style>
  :root {
    --ink: #0b0b0d;
    --night: #05060c;
    --deep-blue: #121a52;
    --violet: #3a2a8c;
    --sky: #29aee6;
    --white: #ffffff;
    --soft-white: #e9ecf3;
    --rule: #d8d8d8;
    --band: #1a1f4a;
    --brand-blue: #2aa7e0;
    --haze-blue: rgba(40, 70, 120, 0.45);
  }
  * { margin: 0; padding: 0; box-sizing: border-box; }
  html, body { width: 902px; height: 1200px; overflow: hidden; background: var(--ink); }
  .invitation {
    position: relative;
    width: 902px;
    height: 1200px;
    overflow: hidden;
    background: var(--ink);
    color: var(--white);
    font-family: "Lato", Arial, sans-serif;
  }
  .space-backdrop {
    position: absolute; inset: 0 0 auto 0; height: 520px;
    background:
      radial-gradient(ellipse 420px 260px at 120px 90px, rgba(40,80,150,0.35), transparent 70%),
      radial-gradient(ellipse 300px 200px at 860px 520px, rgba(150,40,120,0.22), transparent 70%),
      linear-gradient(180deg, #0a0f1c 0%, var(--night) 100%);
  }
  .planet-area {
    position: absolute; left: 740px; top: 70px;
    width: 162px; height: 290px;
    background: linear-gradient(90deg, transparent 0%, var(--haze-blue) 60%, var(--haze-blue) 100%);
  }
  .hub-photo {
    position: absolute; left: 0; top: 486px; width: 902px; height: 310px;
    background:
      radial-gradient(circle 130px at 453px 160px, rgba(120,130,255,0.7), rgba(60,60,200,0.4) 60%, transparent 100%),
      radial-gradient(ellipse 520px 220px at 450px 140px, rgba(58,42,140,0.7), transparent 80%),
      linear-gradient(180deg, #0c0f2a 0%, var(--deep-blue) 35%, #1b1250 70%, var(--ink) 100%);
  }
  .brand {
    position: absolute; top: 160px; left: 0; width: 902px;
    text-align: center;
  }
  .brand-mark { display: inline-flex; align-items: center; gap: 18px; }
  .brand-dot {
    width: 46px; height: 46px; border-radius: 50%;
    background: var(--soft-white);
  }
  .brand-name {
    font-weight: 900; font-size: 96px; letter-spacing: 6px;
    line-height: 1; color: var(--white);
  }
  .brand-tagline {
    margin-top: 20px;
    font-weight: 400; font-size: 30px; color: var(--white);
  }
  .headline {
    position: absolute; top: 340px; left: 0; width: 902px;
    text-align: center;
    font-family: "Lobster Two", "Lobster", cursive;
    font-style: italic; font-weight: 700;
    font-size: 64px; color: var(--sky); line-height: 1.1;
  }
  .intro {
    position: absolute; top: 414px; left: 0; width: 902px;
    text-align: center;
    font-style: italic; font-weight: 700;
    font-size: 26px; line-height: 31px; color: var(--white);
  }
  .details-panel {
    position: absolute; left: 245px; top: 791px; width: 412px; height: 180px;
    background: var(--ink);
    text-align: center;
  }
  .event-date {
    margin-top: 32px;
    font-family: "Lobster", cursive;
    font-size: 36px; color: var(--white); line-height: 1;
  }
  .event-time {
    margin-top: 15px;
    font-family: "Lobster Two", cursive; font-style: italic; font-weight: 700;
    font-size: 22px; line-height: 1;
  }
  .event-address {
    margin: 16px 12px 0; 
    border-top: 1px solid var(--rule); border-bottom: 1px solid var(--rule);
    padding: 10px 0 9px;
    font-family: "Jost", "Futura", sans-serif;
    font-size: 26px; letter-spacing: 1px; text-transform: uppercase; line-height: 1;
  }
  .notes {
    position: absolute; top: 982px; left: 0; width: 902px;
    text-align: center; font-size: 15px; line-height: 19px; color: var(--white);
  }
  .notes p + p { margin-top: 14px; }
  .rsvp-band {
    position: absolute; left: 196px; top: 1110px; width: 706px; height: 56px;
    background: linear-gradient(90deg, var(--band) 0%, #101432 70%, #1a2560 100%);
    display: flex; align-items: center; padding-left: 50px;
    font-size: 19px; color: var(--soft-white);
  }
  .partner-mark {
    position: absolute; left: 98px; top: 1076px; width: 96px; height: 92px;
    background: var(--brand-blue);
    display: flex; align-items: center; justify-content: center; text-align: center;
    font-weight: 900; font-size: 15px; line-height: 18px; color: var(--white);
    padding: 6px;
  }
</style>
</head>
<body>
  <main class="invitation">
    <div class="space-backdrop" role="img" aria-label="Deep space background scattered with soft blue stars"></div>
    <div class="planet-area" role="img" aria-label="Earth seen from space, partly cut off at the right edge"></div>
    <div class="hub-photo" role="img" aria-label="Photo of a glowing plasma globe on a plinth inside the darkened STEM hub"></div>

    <header class="brand">
      <div class="brand-mark">
        <span class="brand-dot"></span>
        <span class="brand-name">LUMEN</span>
      </div>
      <p class="brand-tagline">Centre of Discovery</p>
    </header>

    <h1 class="headline">You’re invited to</h1>
    <p class="intro">the official opening and launch of Lumen, Centre of Discovery.<br>An industry first, pioneering, STEM hub.</p>

    <section class="details-panel">
      <p class="event-date">Saturday 30th April, 2022</p>
      <p class="event-time">10:00 am - 12:00 pm</p>
      <p class="event-address">42 Calder Lane, Wrenfield</p>
    </section>

    <section class="notes">
      <p>Light canapes provided. Dress code is smart/casual</p>
      <p>All guests will be given a guided walk through of Australia’s first<br>dedicated STEM education hub for children aged 3-6.</p>
      <p>Invitation only</p>
    </section>

    <div class="partner-mark">Bloom and Grow</div>
    <footer class="rsvp-band">RSVP: 18 April to marketing@bloomandgrow.edu.au</footer>
  </main>
</body>
</html>
```